Company Holiday Card

Please design a corporate holiday card for our investment firm. Our firm invests in Media & Entertainment assets so incorporating some of that imagery in a creative and festive way would be ideal so that the card doesn't feel so generic.

I have attached some design inspiration that could be cute if we're able to incorporate Media & Entertainment images into those scenes. Things like a film roll, movie cut board, video game console, music notes, sports balls (soccer, football, etc.), event tickets, microphone, kalder, etc. I have also attached two versions of our logo in case that's helpful.

The audience will be private equity investors and counterparties so we would still like to keep it polished and professional.

```html
<!DOCTYPE html>
<html lang="en">
<head>
<meta charset="utf-8">
<title>Holiday Card – Meridian Harbor</title>
<link rel="stylesheet" href="https://fonts.googleapis.com/css2?family=Ultra&family=Libre+Baskerville&family=Barlow:wght@500&display=swap">
<style>
  :root {
    --navy-deep: #111b2a;
    --navy-mid: #14294a;
    --navy-glow: #17315a;
    --teal: #5fc2ab;
    --pink: #f2a3a8;
    --red: #e5494c;
    --white: #f7f7f5;
    --rule: #c9ccd2;
  }
  * { margin: 0; padding: 0; box-sizing: border-box; }
  html, body { width: 857px; height: 1200px; overflow: hidden; background: var(--navy-deep); }
  .card {
    position: relative;
    width: 857px;
    height: 1200px;
    overflow: hidden;
    background:
      radial-gradient(ellipse 60% 45% at 50% 45%, var(--navy-glow) 0%, var(--navy-mid) 45%, var(--navy-deep) 100%);
  }
  .wreath {
    position: absolute;
    left: 78px;
    top: 246px;
    width: 700px;
    height: 700px;
  }
  .greeting {
    position: absolute;
    left: 0;
    width: 100%;
    top: 508px;
    text-align: center;
    color: var(--white);
  }
  .greeting__merry {
    font-family: "Ultra", serif;
    font-size: 55px;
    line-height: 1;
    letter-spacing: 1px;
  }
  .greeting__christmas {
    font-family: "Ultra", serif;
    font-size: 39px;
    line-height: 1;
    margin-top: 10px;
    letter-spacing: 0.5px;
  }
  .greeting__divider {
    display: flex;
    align-items: center;
    justify-content: center;
    gap: 8px;
    margin-top: 6px;
    height: 36px;
  }
  .greeting__line { width: 104px; height: 1px; background: var(--rule); }
  .greeting__dots { font-family: "Libre Baskerville", serif; font-size: 10px; letter-spacing: 2px; color: var(--rule); }
  .greeting__amp { font-family: "Libre Baskerville", serif; font-size: 38px; line-height: 1; }
  .greeting__newyear {
    font-family: "Libre Baskerville", serif;
    font-size: 21px;
    letter-spacing: 6px;
    margin-top: 8px;
    padding-left: 6px;
  }
  .brand {
    position: absolute;
    left: 0;
    width: 100%;
    top: 1108px;
    display: flex;
    align-items: center;
    justify-content: center;
    gap: 14px;
    font-family: "Barlow", sans-serif;
    font-weight: 500;
    font-size: 44px;
    letter-spacing: 2px;
    color: var(--white);
  }
  .brand__mark { width: 14px; height: 14px; background: var(--white); }
</style>
</head>
<body>
  <main class="card">
    <svg class="wreath" viewBox="0 0 700 700" role="img" aria-label="Wreath of media and entertainment icons: film camera, clapperboard, tickets, music notes, headphones, microphones, game controllers, soccer balls, a football, a basketball, a kalder, a leaping reindeer and snowflakes in teal, pink and red">
      <defs>
        <linearGradient id="wreathTone" x1="0" y1="0" x2="1" y2="1">
          <stop offset="0" stop-color="#5fc2ab"/>
          <stop offset="0.35" stop-color="#f2a3a8"/>
          <stop offset="0.6" stop-color="#e5494c"/>
          <stop offset="1" stop-color="#5fc2ab"/>
        </linearGradient>
      </defs>
      <circle cx="350" cy="348" r="268" fill="none" stroke="url(#wreathTone)" stroke-width="160" opacity="0.55"/>
    </svg>

    <section class="greeting">
      <h1 class="greeting__merry">MERRY</h1>
      <h2 class="greeting__christmas">CHRISTMAS</h2>
      <div class="greeting__divider">
        <span class="greeting__line"></span>
        <span class="greeting__dots">····</span>
        <span class="greeting__amp">&amp;</span>
        <span class="greeting__dots">····</span>
        <span class="greeting__line"></span>
      </div>
      <p class="greeting__newyear">HAPPY NEW YEAR</p>
    </section>

    <footer class="brand">
      <span class="brand__mark"></span>
      <span class="brand__name">MERIDIAN HARBOR</span>
    </footer>
  </main>
</body>
</html>
```